Bramblecrest Apparel and Nutrition is looking for a Clothing/Supplement Online Store Website!

Must be convenient, and user friendly, with vibrant colors that catch the eye!

Target Market(s)

Athletes, and Fashion Customers

Industry/Entity Type

Fitness

Coding

Coded - Design and coding required

Number of Pages Required

3 page

Font styles to use
Decorative

Colors

Designer to choose colors to be used in the design.

Requirements
Must have
• Somewhere to feature products, features to promote discounts and make announcements.
Nice to have
• My logos on each page

```html
<!DOCTYPE html>
<html lang="en">
<head>
<meta charset="utf-8">
<title>Bramblecrest Apparel and Nutrition</title>
<link rel="stylesheet" href="https://fonts.googleapis.com/css2?family=Montserrat:wght@600;700;800&family=Open+Sans:wght@400;600;700&family=Kaushan+Script&display=swap">
<style>
:root{
  --slate:#5b5a5f;
  --slate-dark:#3f3f44;
  --ink:#2b2b2e;
  --text:#555559;
  --muted:#9a9a9e;
  --price:#c49a5a;
  --card:#f4f4f5;
  --footer:#f3f4f8;
  --line:#e2e3e8;
  --red:#e2272e;
  --white:#ffffff;
}
*{box-sizing:border-box;margin:0;padding:0}
html,body{width:1200px;height:3125px;overflow:hidden;background:var(--white)}
body{position:relative;font-family:"Open Sans",sans-serif;color:var(--text)}
.abs{position:absolute}
.center-x{transform:translateX(-50%);text-align:center;white-space:nowrap}
.heading{font-family:"Montserrat",sans-serif;font-weight:800;letter-spacing:2px;color:var(--ink)}
.script{font-family:"Kaushan Script",cursive;color:rgba(0,0,0,.07);white-space:nowrap}

/* hero */
.hero{position:absolute;left:0;top:0;width:1200px;height:533px;overflow:hidden}
.brand{font-family:"Montserrat",sans-serif;font-weight:700;color:var(--slate-dark);letter-spacing:1px;white-space:nowrap}
.nav{top:44px;font-family:"Montserrat",sans-serif;font-weight:700;font-size:9px;color:var(--white);letter-spacing:.5px}
.nav.active{border-bottom:1px solid var(--white);padding-bottom:3px}
.icon-btn{width:26px;height:26px;border-radius:50%;background:var(--white);border:1px solid #ddd;display:flex;align-items:center;justify-content:center}
.hero-title{left:413px;top:228px;font-size:36px;color:var(--white)}
.hero-script{left:413px;top:190px;font-size:48px;color:rgba(255,255,255,.08)}
.hero-sub{left:413px;top:271px;font-size:13px;color:var(--white)}
.btn-outline{left:340px;top:307px;width:139px;height:35px;border:2px solid var(--white);border-radius:18px;color:var(--white);font-family:"Montserrat",sans-serif;font-weight:700;font-size:10px;display:flex;align-items:center;justify-content:center}
.dot{width:9px;height:9px;border-radius:50%;background:#eee;top:486px}
.dot.on{background:var(--white);box-shadow:0 0 0 2px rgba(0,0,0,.25) inset}

/* perks */
.perk-title{font-size:10.5px;font-weight:700;color:var(--ink)}
.perk-sub{font-size:9px;color:var(--muted)}
.perk-divider{width:1px;height:25px;background:var(--line)}

/* promos */
.promo{background:#efeff0;width:357px;height:163px;top:671px}
.promo-frame{position:absolute;left:15px;top:12px;right:15px;bottom:12px;border:3px solid var(--white)}
.promo-label{font-family:"Montserrat",sans-serif;font-weight:800;font-size:21px;color:#dedee0;letter-spacing:2px;transform:translate(-50%,-50%) rotate(-90deg);white-space:nowrap}
.promo-pct{font-family:"Montserrat",sans-serif;font-weight:800;font-size:30px;color:var(--red)}
.promo-disc{font-family:"Montserrat",sans-serif;font-weight:800;font-size:12px;color:var(--ink);letter-spacing:.5px}
.promo-note{font-size:9px;color:var(--muted)}
.btn-dark{background:var(--slate);color:var(--white);font-family:"Montserrat",sans-serif;font-weight:700;font-size:8px;display:flex;align-items:center;justify-content:center}
.soft-img{background:radial-gradient(closest-side,var(--tone) 30%,var(--tone-2,transparent) 62%,rgba(255,255,255,0) 100%)}

/* toggle */
.toggle{left:511px;top:985px;width:179px;height:38px;border:1px solid var(--slate);border-radius:19px;overflow:hidden;font-family:"Montserrat",sans-serif;font-weight:700;font-size:9.5px}
.toggle-on{position:absolute;left:0;top:0;width:88px;height:100%;background:var(--slate);color:var(--white);border-radius:19px;display:flex;align-items:center;justify-content:center}
.toggle-off{position:absolute;left:88px;top:0;width:91px;height:100%;color:var(--ink);display:flex;align-items:center;justify-content:center}

/* product grids */
.grid{position:absolute;left:235px;width:732px;display:grid;grid-template-columns:repeat(4,170px);column-gap:17px;row-gap:17px}
.product{height:240px}
.thumb{width:170px;height:170px;background:var(--card);border:1px solid #ececee;display:flex;align-items:center;justify-content:center;overflow:hidden}
.thumb-fill{width:150px;height:150px;background:radial-gradient(closest-side,var(--tone) 38%,rgba(244,244,245,0) 100%)}
.thumb-fill.tub{width:110px;height:150px}
.stars{margin-top:13px;font-size:8px;letter-spacing:1.5px;color:#7a7a7e;line-height:10px}
.pname{margin-top:5px;font-size:10.5px;font-weight:700;color:var(--text);line-height:14px}
.pprice{margin-top:4px;font-size:10px;line-height:14px;white-space:nowrap}
.pprice .now{color:var(--price);font-weight:600}
.pprice .was{color:#b5b5b9;text-decoration:line-through;margin-left:6px}
.pprice .off{color:var(--ink);font-size:8.5px;margin-left:8px}

/* nutrition band */
.band{left:0;width:1200px;background:#58575c}
.band-title{left:871px;top:1784px;font-size:24px;color:var(--white)}
.band-script{left:871px;top:1745px;font-size:50px;color:rgba(255,255,255,.08)}
.band-copy{left:871px;top:1819px;width:400px;font-size:12.5px;line-height:22px;color:var(--white);transform:translateX(-50%);text-align:center}
.btn-white{background:var(--white);color:var(--ink);font-family:"Montserrat",sans-serif;font-weight:700;font-size:9.5px;display:flex;align-items:center;justify-content:center}
.arrow-btn{width:32px;height:32px;border-radius:50%;background:#ededef;display:flex;align-items:center;justify-content:center}

/* newsletter */
.news-title{left:285px;top:2584px;font-size:22px;color:var(--white)}
.news-script{left:262px;top:2547px;font-size:52px;color:rgba(255,255,255,.08)}
.news-input{left:628px;top:2571px;width:250px;height:33px;border:1px solid var(--white);color:var(--white);font-size:9px;padding-left:13px;display:flex;align-items:center}
.news-submit{left:878px;top:2571px;width:74px;height:33px;border:1px solid var(--white);border-left:none;color:var(--white);font-family:"Montserrat",sans-serif;font-weight:700;font-size:10px;display:flex;align-items:center;justify-content:center}

/* footer */
.footer{left:0;top:2806px;width:1200px;height:319px;background:var(--footer)}
.f-head{font-size:10.5px;font-weight:700;color:var(--ink)}
.f-link{font-size:9px;color:var(--text);white-space:nowrap}
.social{width:26px;height:26px;border-radius:50%;background:#505055;border:2px solid #d9d9dd}
.pay{width:32px;height:20px;border-radius:3px}
.legal{font-size:9px;color:var(--text);white-space:nowrap}
.legal u{margin-right:14px}
</style>
</head>
<body>

<!-- HERO -->
<header class="hero">
  <svg class="abs" style="left:0;top:0" width="1200" height="533" viewBox="0 0 1200 533">
    <defs>
      <linearGradient id="sky" x1="0" y1="0" x2="0" y2="1">
        <stop offset="0" stop-color="#5b87c2"/>
        <stop offset=".6" stop-color="#a9c2de"/>
        <stop offset="1" stop-color="#c9b9a3"/>
      </linearGradient>
      <radialGradient id="runner" cx=".5" cy=".5" r=".5">
        <stop offset="0" stop-color="#c94a3e" stop-opacity=".75"/>
        <stop offset=".5" stop-color="#b88a74" stop-opacity=".45"/>
        <stop offset="1" stop-color="#b88a74" stop-opacity="0"/>
      </radialGradient>
    </defs>
    <polygon points="348,0 825,0 494,533 0,533 0,479" fill="#5b5a5f"/>
    <g role="img" aria-label="Photo of a runner in a red athletic tank against a bright sky">
      <polygon points="825,0 1200,0 1200,533 494,533" fill="url(#sky)"/>
      <ellipse cx="820" cy="290" rx="230" ry="300" fill="url(#runner)"/>
    </g>
    <line x1="348" y1="0" x2="0" y2="479" stroke="#d9d9dc" stroke-width="1"/>
  </svg>
  <div class="abs brand" style="left:40px;top:30px;font-size:25px">BRAMBLECREST</div>

  <a class="abs nav active" style="left:387px;transform:translateX(-50%)">HOME</a>
  <a class="abs nav" style="left:473px;transform:translateX(-50%)">ABOUT</a>
  <a class="abs nav" style="left:545px;transform:translateX(-50%)">SHOP</a>
  <a class="abs nav" style="left:615px;transform:translateX(-50%)">BLOG</a>
  <a class="abs nav" style="left:693px;transform:translateX(-50%)">CONTACT</a>

  <div class="abs icon-btn" style="left:1091px;top:42px">
    <svg width="10" height="10" viewBox="0 0 10 10"><circle cx="4" cy="4" r="3" fill="none" stroke="#2b2b2e" stroke-width="1.4"/><line x1="6.2" y1="6.2" x2="9" y2="9" stroke="#2b2b2e" stroke-width="1.4"/></svg>
  </div>
  <div class="abs icon-btn" style="left:1126px;top:42px">
    <svg width="11" height="10" viewBox="0 0 11 10"><path d="M0 1h2l1.5 5h5.5l1.5-4H3" fill="none" stroke="#2b2b2e" stroke-width="1.3"/><rect x="3" y="3" width="6.5" height="2.8" fill="#2b2b2e"/><circle cx="4" cy="8.5" r="1" fill="#2b2b2e"/><circle cx="8.5" cy="8.5" r="1" fill="#2b2b2e"/></svg>
  </div>

  <div class="abs script hero-script center-x">New Look</div>
  <h1 class="abs heading hero-title center-x">POPULAR STYLE</h1>
  <p class="abs hero-sub center-x">Shop the latest fashion trends and styles</p>
  <a class="abs btn-outline">SHOP NOW</a>

  <span class="abs dot on" style="left:580px"></span>
  <span class="abs dot" style="left:595px"></span>
  <span class="abs dot" style="left:612px"></span>
</header>

<!-- PERKS TOP -->
<section class="perks">
  <svg class="abs" style="left:299px;top:581px" width="24" height="24" viewBox="0 0 24 24" fill="none" stroke="#2b2b2e" stroke-width="1.3"><path d="M21 3c-6 0-10 4-13 9l4 4c5-3 9-7 9-13z"/><circle cx="15" cy="9" r="1.8"/><path d="M8 12l-4 1 2-4 4-1M12 16l-1 4 4-2 1-4M6 18l-3 3"/></svg>
  <div class="abs perk-title" style="left:336px;top:580px">Free Shipping Worldwide</div>
  <div class="abs perk-sub" style="left:336px;top:595px">on order over $100</div>
  <div class="abs perk-divider" style="left:483px;top:582px"></div>

  <svg class="abs" style="left:533px;top:581px" width="24" height="24" viewBox="0 0 24 24" fill="none" stroke="#2b2b2e" stroke-width="1.3"><path d="M4 14v-2a8 8 0 0116 0v2"/><rect x="3" y="13" width="4" height="6" rx="1.5"/><rect x="17" y="13" width="4" height="6" rx="1.5"/><path d="M19 19c0 2-2 3-5 3h-2"/></svg>
  <div class="abs perk-title" style="left:567px;top:580px">Online 24/7 support</div>
  <div class="abs perk-sub" style="left:567px;top:595px">signup for gift</div>
  <div class="abs perk-divider" style="left:715px;top:582px"></div>

  <svg class="abs" style="left:749px;top:583px" width="26" height="20" viewBox="0 0 26 20" fill="none" stroke="#2b2b2e" stroke-width="1.3"><rect x="1" y="3" width="15" height="11"/><path d="M16 7h5l4 4v3h-9"/><circle cx="6" cy="16" r="2" fill="#fff"/><circle cx="20" cy="16" r="2" fill="#fff"/></svg>
  <div class="abs perk-title" style="left:785px;top:580px">14-Days Money Back</div>
  <div class="abs perk-sub" style="left:785px;top:595px">best deal with 30days</div>
</section>

<!-- PROMOS -->
<section class="promos">
  <div class="abs promo" style="left:235px"><div class="promo-frame"></div></div>
  <div class="abs promo-label" style="left:291px;top:752px">APPAREL</div>
  <div class="abs soft-img" role="img" aria-label="Photo of a runner in a white tank and dark shorts" style="left:300px;top:650px;width:140px;height:215px;--tone:rgba(120,122,135,.55);--tone-2:rgba(200,200,205,.35)"></div>
  <div class="abs promo-pct center-x" style="left:491px;top:702px">30%</div>
  <div class="abs promo-disc center-x" style="left:491px;top:742px">DISCOUNT</div>
  <div class="abs promo-note center-x" style="left:491px;top:757px">Shop Online &amp; Store</div>
  <a class="abs btn-dark" style="left:456px;top:778px;width:71px;height:20px">SHOP NOW</a>

  <div class="abs promo" style="left:610px"><div class="promo-frame"></div></div>
  <div class="abs promo-label" style="left:666px;top:752px">NUTRITION</div>
  <div class="abs soft-img" role="img" aria-label="Photo of a cyan protein powder tub" style="left:690px;top:645px;width:120px;height:175px;--tone:rgba(40,185,225,.85);--tone-2:rgba(40,185,225,.3)"></div>
  <div class="abs promo-pct center-x" style="left:865px;top:702px">30%</div>
  <div class="abs promo-disc center-x" style="left:865px;top:742px">DISCOUNT</div>
  <div class="abs promo-note center-x" style="left:865px;top:757px">Shop Online &amp; Store</div>
  <a class="abs btn-dark" style="left:830px;top:778px;width:71px;height:20px">SHOP NOW</a>
</section>

<!-- FEATURE PRODUCTS -->
<section class="feature">
  <div class="abs script center-x" style="left:600px;top:896px;font-size:48px">Products</div>
  <h2 class="abs heading center-x" style="left:600px;top:930px;font-size:21px">FEATURE&nbsp; PRODUCTS</h2>
  <div class="abs toggle"><span class="toggle-on">APPAREL</span><span class="toggle-off">NUTRITION</span></div>

  <div class="grid" style="top:1091px">
    <article class="product"><div class="thumb"><div class="thumb-fill" role="img" aria-label="Charcoal hoodie" style="--tone:#5a5f68"></div></div><div class="stars">★★★★★</div><div class="pname">Bramblecrest Apparel</div><div class="pprice"><span class="now">$110.00</span><span class="was">$722.00</span><span class="off">85%</span></div></article>
    <article class="product"><div class="thumb"><div class="thumb-fill" role="img" aria-label="Grey and white long sleeve jersey" style="--tone:#b4b4b7"></div></div><div class="stars">★★★★★</div><div class="pname">Bramblecrest Apparel</div><div class="pprice"><span class="now">$110.00</span><span class="was">$722.00</span><span class="off">85%</span></div></article>
    <article class="product"><div class="thumb"><div class="thumb-fill" role="img" aria-label="Green t-shirt" style="--tone:#2a6e3d"></div></div><div class="stars">★★★★★</div><div class="pname">Bramblecrest Apparel</div><div class="pprice"><span class="now">$110.00</span><span class="was">$722.00</span><span class="off">85%</span></div></article>
    <article class="product"><div class="thumb"><div class="thumb-fill" role="img" aria-label="Blue long sleeve top" style="--tone:#7596d8"></div></div><div class="stars">★★★★★</div><div class="pname">Bramblecrest Apparel</div><div class="pprice"><span class="now">$110.00</span><span class="was">$722.00</span><span class="off">85%</span></div></article>
    <article class="product"><div class="thumb"><div class="thumb-fill" role="img" aria-label="Dark grey t-shirt" style="--tone:#635f5f"></div></div><div class="stars">★★★★★</div><div class="pname">Bramblecrest Apparel</div><div class="pprice"><span class="now">$110.00</span><span class="was">$722.00</span><span class="off">85%</span></div></article>
    <article class="product"><div class="thumb"><div class="thumb-fill" role="img" aria-label="Light grey printed t-shirt" style="--tone:#a0a4a6"></div></div><div class="stars">★★★★★</div><div class="pname">Bramblecrest Apparel</div><div class="pprice"><span class="now">$110.00</span><span class="was">$722.00</span><span class="off">85%</span></div></article>
    <article class="product"><div class="thumb"><div class="thumb-fill" role="img" aria-label="Heather grey t-shirt" style="--tone:#858585"></div></div><div class="stars">★★★★★</div><div class="pname">Bramblecrest Apparel</div><div class="pprice"><span class="now">$110.00</span><span class="was">$722.00</span><span class="off">85%</span></div></article>
    <article class="product"><div class="thumb"><div class="thumb-fill" role="img" aria-label="Black long sleeve top" style="--tone:#2a2f2d"></div></div><div class="stars">★★★★★</div><div class="pname">Bramblecrest Apparel</div><div class="pprice"><span class="now">$110.00</span><span class="was">$722.00</span><span class="off">85%</span></div></article>
  </div>
</section>

<!-- NUTRITION BAND -->
<section class="nutrition">
  <div class="abs band" style="top:1650px;height:374px"></div>
  <div class="abs" role="img" aria-label="Photo of a sprinter in white kit crouched at the start line" style="left:90px;top:1640px;width:560px;height:400px;background:radial-gradient(closest-side,rgba(236,236,238,.85) 25%,rgba(200,200,204,.45) 65%,rgba(88,87,92,0) 100%)"></div>
  <div class="abs" style="left:380px;top:1739px;width:234px;height:234px;border-radius:50%;background:rgba(255,255,255,.55)"></div>
  <div class="abs" role="img" aria-label="Photo of a green protein powder tub" style="left:425px;top:1765px;width:160px;height:235px;background:radial-gradient(closest-side,rgba(72,190,72,.95) 35%,rgba(72,190,72,.35) 70%,rgba(72,190,72,0) 100%)"></div>

  <div class="abs script band-script center-x">Nutrition</div>
  <h2 class="abs heading band-title center-x">NUTRITION PRODUCTS</h2>
  <p class="abs band-copy">We have limited time offerings for our special suppliment that goes with a special offer. Grab now!</p>
  <a class="abs btn-white" style="left:830px;top:1881px;width:93px;height:26px">SHOP NOW!</a>
</section>

<!-- BEST PRODUCTS -->
<section class="best">
  <div class="abs script center-x" style="left:600px;top:2118px;font-size:48px">Products</div>
  <h2 class="abs heading center-x" style="left:600px;top:2152px;font-size:21px">BEST&nbsp; PRODUCTS</h2>

  <div class="abs arrow-btn" style="left:158px;top:2280px"><svg width="8" height="10" viewBox="0 0 8 10"><path d="M6 1L2 5l4 4" fill="none" stroke="#2b2b2e" stroke-width="1.4"/></svg></div>
  <div class="abs arrow-btn" style="left:1010px;top:2280px"><svg width="8" height="10" viewBox="0 0 8 10"><path d="M2 1l4 4-4 4" fill="none" stroke="#2b2b2e" stroke-width="1.4"/></svg></div>

  <div class="grid" style="top:2213px">
    <article class="product"><div class="thumb"><div class="thumb-fill" role="img" aria-label="Charcoal hoodie" style="--tone:#5a5f68"></div></div><div class="stars">★★★★★</div><div class="pname">Bramblecrest Apparel</div><div class="pprice"><span class="now">$110.00</span><span class="was">$722.00</span><span class="off">85%</span></div></article>
    <article class="product"><div class="thumb"><div class="thumb-fill tub" role="img" aria-label="Green protein powder tub" style="--tone:#4cbf4a"></div></div><div class="stars">★★★★★</div><div class="pname">Bramblecrest Nutrition</div><div class="pprice"><span class="now">$110.00</span><span class="was">$722.00</span><span class="off">85%</span></div></article>
    <article class="product"><div class="thumb"><div class="thumb-fill" role="img" aria-label="Green t-shirt" style="--tone:#2a6e3d"></div></div><div class="stars">★★★★★</div><div class="pname">Bramblecrest Apparel</div><div class="pprice"><span class="now">$110.00</span><span class="was">$722.00</span><span class="off">85%</span></div></article>
    <article class="product"><div class="thumb"><div class="thumb-fill tub" role="img" aria-label="Pink protein powder tub" style="--tone:#e23a6e"></div></div><div class="stars">★★★★★</div><div class="pname">Bramblecrest Nutrition</div><div class="pprice"><span class="now">$110.00</span><span class="was">$722.00</span><span class="off">85%</span></div></article>
  </div>
</section>

<!-- NEWSLETTER -->
<section class="newsletter">
  <div class="abs band" style="top:2507px;height:155px"></div>
  <div class="abs script news-script">Newsletter</div>
  <h2 class="abs heading news-title">GET DISCOUNT INFO</h2>
  <div class="abs news-input">Enter your email address</div>
  <a class="abs news-submit">SUBMIT</a>
</section>

<!-- PERKS BOTTOM -->
<section class="perks">
  <svg class="abs" style="left:299px;top:2717px" width="24" height="24" viewBox="0 0 24 24" fill="none" stroke="#2b2b2e" stroke-width="1.3"><path d="M21 3c-6 0-10 4-13 9l4 4c5-3 9-7 9-13z"/><circle cx="15" cy="9" r="1.8"/><path d="M8 12l-4 1 2-4 4-1M12 16l-1 4 4-2 1-4M6 18l-3 3"/></svg>
  <div class="abs perk-title" style="left:336px;top:2716px">Free Shipping Worldwide</div>
  <div class="abs perk-sub" style="left:336px;top:2731px">on order over $100</div>
  <div class="abs perk-divider" style="left:483px;top:2718px"></div>

  <svg class="abs" style="left:533px;top:2717px" width="24" height="24" viewBox="0 0 24 24" fill="none" stroke="#2b2b2e" stroke-width="1.3"><path d="M4 14v-2a8 8 0 0116 0v2"/><rect x="3" y="13" width="4" height="6" rx="1.5"/><rect x="17" y="13" width="4" height="6" rx="1.5"/><path d="M19 19c0 2-2 3-5 3h-2"/></svg>
  <div class="abs perk-title" style="left:567px;top:2716px">Online 24/7 support</div>
  <div class="abs perk-sub" style="left:567px;top:2731px">signup for gift</div>
  <div class="abs perk-divider" style="left:715px;top:2718px"></div>

  <svg class="abs" style="left:749px;top:2719px" width="26" height="20" viewBox="0 0 26 20" fill="none" stroke="#2b2b2e" stroke-width="1.3"><rect x="1" y="3" width="15" height="11"/><path d="M16 7h5l4 4v3h-9"/><circle cx="6" cy="16" r="2" fill="#fff"/><circle cx="20" cy="16" r="2" fill="#fff"/></svg>
  <div class="abs perk-title" style="left:785px;top:2716px">14-Days Money Back</div>
  <div class="abs perk-sub" style="left:785px;top:2731px">best deal with 30days</div>
</section>

<!-- FOOTER -->
<footer class="abs footer">
  <div class="abs" style="left:450px;top:0;width:1px;height:258px;background:var(--line)"></div>
  <div class="abs" style="left:0;top:258px;width:1200px;height:1px;background:var(--line)"></div>

  <div class="abs f-head" style="left:235px;top:49px">Contact Info</div>
  <div class="abs f-link" style="left:235px;top:79px">Phone: +00 5550 129 874</div>
  <div class="abs f-link" style="left:235px;top:102px">Address: Bramblecrest Apparel and Nutrition</div>
  <div class="abs f-link" style="left:235px;top:124px">Mail: info@bramblecrest.com</div>
  <div class="abs f-head" style="left:235px;top:168px">Follow Us</div>
  <span class="abs social" style="left:235px;top:194px"></span>
  <span class="abs social" style="left:266px;top:194px"></span>
  <span class="abs social" style="left:299px;top:194px"></span>
  <span class="abs social" style="left:330px;top:194px"></span>

  <div class="abs f-head" style="left:485px;top:49px">Information</div>
  <div class="abs f-link" style="left:485px;top:79px">About Us</div>
  <div class="abs f-link" style="left:485px;top:102px">Delivery Information</div>
  <div class="abs f-link" style="left:485px;top:124px">Privacy Policy</div>
  <div class="abs f-link" style="left:485px;top:147px">Terms &amp; Conditions</div>
  <div class="abs f-link" style="left:485px;top:170px">Brands</div>

  <div class="abs f-head" style="left:624px;top:49px">My Account</div>
  <div class="abs f-link" style="left:624px;top:79px">Brands</div>
  <div class="abs f-link" style="left:624px;top:102px">Affiliate</div>
  <div class="abs f-link" style="left:624px;top:124px">Site Map</div>
  <div class="abs f-link" style="left:624px;top:147px">Specials</div>
  <div class="abs f-link" style="left:624px;top:170px">My Account</div>

  <div class="abs f-head" style="left:736px;top:49px">Extras</div>
  <div class="abs f-link" style="left:736px;top:79px">Specials</div>
  <div class="abs f-link" style="left:736px;top:102px">Gift Certificates</div>
  <div class="abs f-link" style="left:736px;top:124px">Brands</div>
  <div class="abs f-link" style="left:736px;top:147px">Affiliate</div>
  <div class="abs f-link" style="left:736px;top:170px">Site Map</div>

  <div class="abs f-head" style="left:853px;top:49px">Quick Links</div>
  <div class="abs f-link" style="left:853px;top:79px">Brands</div>
  <div class="abs f-link" style="left:853px;top:102px">Affiliate</div>
  <div class="abs f-link" style="left:853px;top:124px">Site Map</div>
  <div class="abs f-link" style="left:853px;top:147px">Specials</div>
  <div class="abs f-link" style="left:853px;top:170px">Gift Certificates</div>

  <div class="abs legal" style="left:231px;top:275px">Copyright © Bramblecrest 2019. All Rights Reserved.</div>
  <div class="abs legal" style="left:231px;top:290px"><u>Terms &amp; Conditions</u><u>Privacy Policy</u></div>

  <div class="abs brand center-x" style="left:600px;top:278px;font-size:18px">BRAMBLECREST</div>

  <span class="abs pay" style="left:850px;top:279px;background:#d9dbe6"></span>
  <span class="abs pay" style="left:892px;top:279px;background:#f2c9b8"></span>
  <span class="abs pay" style="left:935px;top:279px;background:#f3dcc6"></span>
</footer>

</body>
</html>
```